Brochure / Leaflet Required

Hi!
We need a cool brochure / leaflet for our Plexon product line.
These are plastic corrugated sheets which are used to make various products.
When you look at the Plexon section on our website: http://velmarto.example/plexon/ you will get a bit more info (the website is under construction).
We need a separate page for a few products.
But for now we need just one test page for the first product group "Surface Protection". If your design is approved as a template, we will give you the text and pics for the other products. We can set a price per page for the other pages later.
Requirements:
- Size should be A4. The leaflet will be combined into one full brochure at the end. But each page will also need to function a a separate leaflet for that particular product. (For example it will also be placed on the website as a downloadable PDF)
- Font needs to be Gill Sans MT
- This is the brand logo: https://files.quorvik.example/s/k2b81tdex9ma3q1/Plexon%20logo%20-%20registered.ai?dl=0
- These 3 pics should be use on leaflet: https://files.quorvik.example/sh/71xq4mbn2vk8r0w/BBDm8upSwgoMvYZ3LLx5rRhWb?dl=0
- Here you can find the text: https://files.quorvik.example/s/p9h27wlcrzt45ej/Text%20-%20Surface%20Protection.docx?dl=0
- The icons in this text part (including text) also need to be placed in the brochure. The originals can be found here: https://files.quorvik.example/sh/83jm51640hgo2tz/BBEqtZZZ3xxt3NbAxaznv6nLb?dl=0
Please think outside of the box as much as possible.
And make sure to use mainly white and the "Plexon logo" blue.
We also have another product group which will need to be done after this project.
Looking forward to your design!
Regards,
Teun
Target Market(s)
Construction
Industry/Entity Type
Plastic
Look and feel

```html
<!DOCTYPE html>
<html lang="en">
<head>
<meta charset="utf-8">
<title>Plexon Surface Protection Leaflet</title>
<link href="https://fonts.googleapis.com/css2?family=Cabin:wght@400;600;700&display=swap" rel="stylesheet">
<style>
  :root {
    --backdrop: #e6e6e6;
    --paper: #f7f7f7;
    --band: #d2d2d2;
    --strip: #dcdcdc;
    --stripe: #ebebeb;
    --text: #5a5a5a;
    --heading: #4d4d4d;
    --brand-blue: #2f7cc6;
    --rule: #a9a9a9;
  }
  * { box-sizing: border-box; margin: 0; padding: 0; }
  html, body { width: 1200px; height: 1008px; overflow: hidden; }
  body {
    background: var(--backdrop);
    font-family: "Cabin", sans-serif;
    color: var(--text);
  }
  .leaflet {
    position: absolute;
    left: 260px; top: 24px;
    width: 680px; height: 960px;
    background: var(--paper);
    overflow: hidden;
    box-shadow: 0 2px 10px rgba(0,0,0,.12);
  }
  .side-strip {
    position: absolute; left: 0; top: 0; bottom: 0; width: 56px;
    background: var(--strip);
  }
  .intro-band {
    position: absolute; left: 0; right: 0; top: 0; height: 150px;
    background: var(--band);
    padding: 26px 36px 0 110px;
    font-size: 12.5px; line-height: 1.45; text-align: justify;
  }
  .intro-band p + p { margin-top: 6px; }
  .intro-band strong { font-weight: 700; }
  .spec-title {
    position: absolute; left: 76px; top: 166px;
    font-size: 24px; font-weight: 700; color: var(--heading);
  }
  .spec-list { position: absolute; left: 0; right: 0; top: 208px; list-style: none; }
  .spec-item { position: relative; height: 76px; padding: 0 36px 0 76px; }
  .spec-item:nth-child(odd) .spec-body { background: var(--stripe); }
  .spec-icon {
    position: absolute; left: 36px; top: 0; width: 28px; height: 28px;
  }
  .spec-name {
    display: block; height: 26px; line-height: 28px;
    font-size: 14px; font-weight: 600; color: var(--brand-blue);
  }
  .spec-body {
    margin-left: -8px; padding: 5px 8px 6px;
    font-size: 12px; line-height: 1.45; min-height: 44px;
  }
  .divider {
    position: absolute; left: 76px; right: 76px; top: 842px; height: 8px;
  }
  .divider::before {
    content: ""; position: absolute; left: 0; right: 0; top: 3px; height: 1.5px; background: var(--rule);
  }
  .divider::after {
    content: ""; position: absolute; left: 50%; top: 0; width: 8px; height: 8px;
    margin-left: -4px; border-radius: 50%; background: var(--rule);
  }
  .brand-name {
    position: absolute; left: 0; right: 0; top: 872px; text-align: center;
    font-size: 46px; font-weight: 600; color: var(--brand-blue); letter-spacing: 1px;
  }
</style>
</head>
<body>
<main class="leaflet">
  <div class="side-strip"></div>

  <section class="intro-band">
    <p><strong>Plexon sheets</strong> are used for temporary floor and wall protection. The plastic corrugated sheets are designed to provide reusable surface protection for many fixtures and surfaces during construction. The sheets offer excellent surface protection for surfaces like concrete, tile, vinyl, wooden floors, doors, counters, and cabinets. The sheets are easy to apply and cost-effective.</p>
    <p><strong>Plexon sheets</strong> are similar to Flutex sheets are also sold in by the name of PP hollow sheets, twinwallsheets, fluted boards and polypropylene corrugated sheets.</p>
  </section>

  <h1 class="spec-title">Plexon Specifications:</h1>

  <ol class="spec-list">
    <li class="spec-item">
      <svg class="spec-icon" viewBox="0 0 28 28"><circle cx="14" cy="14" r="13" fill="#2f7cc6"/><path d="M11 20l6-12" stroke="#fff" stroke-width="2.2" stroke-linecap="round"/></svg>
      <span class="spec-name">Thickness</span>
      <p class="spec-body">Plexon sheets can be produced in a thickness between 1.5 and 10 mm. We can advise you on what thickness to choose depending on the purpose of use.</p>
    </li>
    <li class="spec-item">
      <svg class="spec-icon" viewBox="0 0 28 28"><circle cx="14" cy="14" r="13" fill="#2f7cc6"/><path d="M8 19h12l-2-8h-8z" fill="#fff"/><circle cx="14" cy="9" r="2" fill="none" stroke="#fff" stroke-width="1.5"/></svg>
      <span class="spec-name">Weight</span>
      <p class="spec-body">The weight of Plexon sheets is expressed in GSM (grams per square meter). The higher you choose your GSM, the stronger and stiffer the material will be.</p>
    </li>
    <li class="spec-item">
      <svg class="spec-icon" viewBox="0 0 28 28"><circle cx="14" cy="14" r="13" fill="#2f7cc6"/><rect x="8" y="8" width="12" height="12" fill="none" stroke="#fff" stroke-width="1.8"/><path d="M11 17l6-6" stroke="#fff" stroke-width="1.5"/></svg>
      <span class="spec-name">Size</span>
      <p class="spec-body">Plexon sheets are available in any requested size. The length can be as long as required; the width is limited to 240 cm.</p>
    </li>
    <li class="spec-item">
      <svg class="spec-icon" viewBox="0 0 28 28"><circle cx="14" cy="14" r="13" fill="#2f7cc6"/><path d="M14 7c-3 4-5 7-5 9a5 5 0 0 0 10 0c0-2-2-5-5-9z" fill="#fff"/></svg>
      <span class="spec-name">color</span>
      <p class="spec-body">Our customers can choose any color for the sheets or artwork. Just ask us what you need, and we can provide you with a sample</p>
    </li>
    <li class="spec-item">
      <svg class="spec-icon" viewBox="0 0 28 28"><circle cx="14" cy="14" r="13" fill="#2f7cc6"/><path d="M9 17a6 6 0 0 1 9-7M19 11a6 6 0 0 1-9 7" fill="none" stroke="#fff" stroke-width="1.8"/><path d="M18 7v4h-4" fill="none" stroke="#fff" stroke-width="1.6"/></svg>
      <span class="spec-name">Virgin and Recycled Polypropylene</span>
      <p class="spec-body">We can use 100% virgin polypropylene to produce your sheets. Another option is to let us recycle up to 20% of our internally regenerated polypropylene.</p>
    </li>
    <li class="spec-item">
      <svg class="spec-icon" viewBox="0 0 28 28"><circle cx="14" cy="14" r="13" fill="#2f7cc6"/><rect x="9" y="8" width="10" height="4" fill="#fff"/><rect x="7" y="12" width="14" height="6" rx="1" fill="#fff"/><rect x="10" y="16" width="8" height="4" fill="#2f7cc6" stroke="#fff" stroke-width="1.2"/></svg>
      <span class="spec-name">Custom Printing</span>
      <p class="spec-body">Plexon sheets can be supplied with high-resolution, full-color printing. Send us your design, and we can directly print it onto the sheets in our factory.</p>
    </li>
    <li class="spec-item">
      <svg class="spec-icon" viewBox="0 0 28 28"><circle cx="14" cy="14" r="13" fill="#2f7cc6"/><path d="M14 6c1 4 5 6 5 10a5 5 0 0 1-10 0c0-2 1-3 2-4 0 2 1 3 2 3 0-3 0-6 1-9z" fill="#fff"/></svg>
      <span class="spec-name">Fire-Retardant Sheets</span>
      <p class="spec-body">A fire-retardant version of Plexon sheets is available. Please let us know the fire rating you require, and we are happy to produce them for you.</p>
    </li>
  </ol>

  <div class="divider"></div>
  <div class="brand-name">Plexon</div>
</main>
</body>
</html>
```